Rocket business card

Modern business card design, use of color is good with clean space too.

Things to include on card:

Quote: I add fuel to your optometry practice

- Eyewear Sales
- Admin Duties
- Revenue Collection
- Leadership
- Tech Adoption
- COGS Reduction
- Product Sourcing
-Medical Growth

Dalton Vessey, CEO
Glint Harbor
Text Me! 847-302-1964
dalton@glintharbor.example

```html
<!DOCTYPE html>
<html lang="en">
<head>
<meta charset="utf-8">
<title>Glint Harbor – Business Card</title>
<link rel="stylesheet" href="https://fonts.googleapis.com/css2?family=Lato:wght@400;700&display=swap">
<style>
  :root {
    --backdrop: #d9d9d9;
    --card: #000000;
    --orange: #f07a1e;
    --red: #e0363a;
    --text: #e6e6e6;
    --muted: #bdbdbd;
    --rule: #8a8a8a;
  }
  * { margin: 0; padding: 0; box-sizing: border-box; }
  html, body { width: 1200px; height: 802px; overflow: hidden; }
  body {
    background: var(--backdrop);
    font-family: "Lato", sans-serif;
    position: relative;
  }
  .card {
    position: absolute;
    top: 237px;
    width: 552px;
    height: 328px;
    background: var(--card);
    overflow: hidden;
    box-shadow: 3px 4px 8px rgba(0,0,0,0.35);
  }
  .card-front { left: 32px; }
  .card-back { left: 616px; }

  .rocket-art {
    position: absolute;
    left: 0; top: 0;
    width: 552px; height: 328px;
  }
  .contact {
    position: absolute;
    left: 28px;
    top: 28px;
    color: var(--text);
  }
  .contact-name {
    color: var(--orange);
    font-weight: 700;
    font-size: 22px;
    letter-spacing: 0.2px;
    line-height: 1.1;
  }
  .contact-title {
    font-size: 17px;
    color: var(--muted);
    line-height: 1.2;
    margin-bottom: 10px;
  }
  .contact-line {
    font-size: 16.5px;
    line-height: 22px;
  }
  .contact-line .label { color: var(--orange); }
  .contact-rule {
    width: 192px;
    height: 1px;
    background: var(--rule);
    margin: 12px 0 10px;
  }
  .services { list-style: none; }
  .services li {
    font-size: 15px;
    line-height: 19.5px;
    padding-left: 16px;
    position: relative;
  }
  .services li::before {
    content: "";
    position: absolute;
    left: 3px; top: 5px;
    width: 8px; height: 8px;
    border-radius: 50%;
    background: var(--orange);
  }

  .brand {
    position: absolute;
    left: 0; right: 0;
    top: 118px;
    display: flex;
    justify-content: center;
    align-items: center;
    gap: 14px;
  }
  .brand-mark {
    width: 30px; height: 30px;
    border-radius: 50%;
    background: var(--orange);
  }
  .brand-name {
    color: #ffffff;
    font-weight: 400;
    font-size: 38px;
    letter-spacing: 2px;
    text-transform: uppercase;
  }
  .tagline {
    position: absolute;
    left: 0; right: 0;
    top: 230px;
    text-align: center;
    color: var(--orange);
    font-weight: 700;
    font-size: 15px;
    letter-spacing: 0.1px;
    text-transform: uppercase;
  }
</style>
</head>
<body>
  <section class="card card-front">
    <svg class="rocket-art" viewBox="0 0 552 328" role="img" aria-label="Rocket illustration on a red-to-orange planet">
      <defs>
        <linearGradient id="planetGlow" x1="0" y1="0" x2="1" y2="0">
          <stop offset="0" stop-color="#e0363a"/>
          <stop offset="1" stop-color="#f28a22"/>
        </linearGradient>
      </defs>
      <circle cx="468" cy="177" r="202" fill="url(#planetGlow)"/>
    </svg>
    <div class="contact">
      <h1 class="contact-name">DALTON VESSEY</h1>
      <p class="contact-title">CEO</p>
      <p class="contact-line"><span class="label">Text Me!</span> 847-302-1964</p>
      <p class="contact-line">dalton@glintharbor.example</p>
      <div class="contact-rule"></div>
      <ul class="services">
        <li>Eyewear Sales</li>
        <li>Admin Duties</li>
        <li>Revenue Collection</li>
        <li>Leadership</li>
        <li>Tech Adoption</li>
        <li>COGS Reduction</li>
        <li>Product Sourcing</li>
        <li>Medical Growth</li>
      </ul>
    </div>
  </section>

  <section class="card card-back">
    <div class="brand">
      <span class="brand-mark"></span>
      <span class="brand-name">Glint Harbor</span>
    </div>
    <p class="tagline">I add fuel to your optometry practice</p>
  </section>
</body>
</html>
```